Brindlewort Organic

Please find attached screenshots of a same product as what I'm selling, looking for similar packaging but yet a whole new different design with my own logo plumtiles which is also attached. It will be on white bags with the clear on the bottom center. As far as colors maby green yellow and black or if you have a better idea. Also it needs to be something that looks up to date modern I like when it has that two-tone gloss to it where it goes from darker to lighter.

```html
<!DOCTYPE html>
<html lang="en">
<head>
<meta charset="utf-8">
<title>Brindlewort Organic – Pouch Front</title>
<link rel="stylesheet" href="https://fonts.googleapis.com/css2?family=Oswald:wght@500;600&family=Montserrat:wght@500;700;800&display=swap">
<style>
  :root {
    --backdrop: #c9c9c9;
    --bag-white: #ffffff;
    --bag-white-shade: #eef0ec;
    --green-deep: #0d4f27;
    --green-mid: #1b7f45;
    --green-light: #4cb860;
    --yellow: #f2c318;
    --yellow-deep: #d9a40c;
    --black: #111111;
    --charcoal: #3a3a3a;
    --white: #ffffff;
    --herb-dark: #3b2a12;
    --herb-olive: #6a5a24;
  }
  * { margin: 0; padding: 0; box-sizing: border-box; }
  html, body { width: 1200px; height: 909px; overflow: hidden; }
  body { background: var(--backdrop); position: relative; }

  .pouch {
    position: absolute; left: 369px; top: 118px;
    width: 465px; height: 665px; overflow: hidden;
    background: linear-gradient(90deg, var(--bag-white-shade), var(--bag-white) 45%, var(--bag-white-shade));
  }
  .pouch__bands { position: absolute; left: 0; top: 0; width: 465px; height: 665px; }

  .tear-line {
    position: absolute; left: 12px; right: 0; top: 58px;
    border-top: 1.5px dashed var(--white);
  }
  .tear-line__icon { position: absolute; left: 8px; top: -9px; }

  .brand {
    position: absolute; left: 0; width: 465px; top: 118px;
    display: flex; align-items: center; justify-content: center; gap: 12px;
  }
  .brand__dot { width: 26px; height: 26px; border-radius: 50%; background: var(--yellow); }
  .brand__name {
    font-family: "Montserrat", sans-serif; font-weight: 800;
    font-size: 34px; letter-spacing: 1px; color: var(--white); line-height: 1;
  }

  .cert-badge {
    position: absolute; left: 372px; top: 170px;
    width: 62px; height: 62px; border-radius: 50%;
    background: var(--white); border: 4px solid var(--yellow);
  }

  .grade { position: absolute; left: 0; width: 465px; top: 254px; text-align: center; }
  .grade__cut {
    font-family: "Montserrat", sans-serif; font-weight: 700; font-size: 14px;
    letter-spacing: 3px; color: var(--black);
    display: inline-block; padding-bottom: 4px; border-bottom: 3px solid var(--yellow);
  }
  .grade__organic {
    font-family: "Montserrat", sans-serif; font-weight: 700; font-size: 20px;
    letter-spacing: 4px; color: var(--green-mid); line-height: 1; margin-top: 6px;
  }

  .product { position: absolute; left: 0; width: 465px; top: 316px; text-align: center; }
  .product__name {
    font-family: "Oswald", sans-serif; font-weight: 600;
    font-size: 62px; line-height: 1; color: var(--black); letter-spacing: 1px;
  }
  .product__sub {
    font-family: "Montserrat", sans-serif; font-weight: 800; font-size: 22px;
    letter-spacing: 6px; color: var(--green-mid); line-height: 1; margin-top: 6px;
  }

  .clear-window {
    position: absolute; left: 142px; top: 470px;
    width: 180px; height: 140px; border-radius: 90px 90px 24px 24px;
    border: 2px solid rgba(255,255,255,.55);
    background:
      linear-gradient(160deg, rgba(255,255,255,.28), rgba(255,255,255,0) 40%),
      radial-gradient(circle at 45% 55%, var(--herb-olive), var(--herb-dark) 75%);
  }

  .net-weight {
    position: absolute; left: 0; width: 465px; top: 628px; text-align: center;
    font-family: "Montserrat", sans-serif; font-weight: 500; font-size: 14px;
    letter-spacing: 1px; color: var(--white);
  }
</style>
</head>
<body>
  <main class="pouch">
    <svg class="pouch__bands" viewBox="0 0 465 665" aria-hidden="true">
      <defs>
        <linearGradient id="greenGloss" x1="0" y1="0" x2="1" y2="1">
          <stop offset="0" stop-color="#0d4f27"/>
          <stop offset=".55" stop-color="#1b7f45"/>
          <stop offset="1" stop-color="#4cb860"/>
        </linearGradient>
        <linearGradient id="blackGloss" x1="0" y1="0" x2="1" y2="1">
          <stop offset="0" stop-color="#3a3a3a"/>
          <stop offset=".5" stop-color="#1a1a1a"/>
          <stop offset="1" stop-color="#0b0b0b"/>
        </linearGradient>
      </defs>
      <path d="M0 0 H465 V200 Q232 270 0 200 Z" fill="url(#greenGloss)"/>
      <path d="M0 200 Q232 270 465 200 V210 Q232 280 0 210 Z" fill="#f2c318"/>
      <path d="M0 440 Q232 410 465 440 V665 H0 Z" fill="#f2c318"/>
      <path d="M0 448 Q232 418 465 448 V665 H0 Z" fill="url(#blackGloss)"/>
    </svg>

    <div class="tear-line">
      <svg class="tear-line__icon" width="18" height="16" viewBox="0 0 18 16" aria-hidden="true">
        <circle cx="4" cy="4" r="3" fill="none" stroke="#ffffff" stroke-width="1.5"/>
        <circle cx="4" cy="12" r="3" fill="none" stroke="#ffffff" stroke-width="1.5"/>
        <path d="M6 5 L17 13 M6 11 L17 3" stroke="#ffffff" stroke-width="1.5"/>
      </svg>
    </div>

    <div class="brand">
      <span class="brand__dot"></span>
      <span class="brand__name">plumtiles</span>
    </div>

    <div class="cert-badge" aria-hidden="true"></div>

    <div class="grade">
      <div class="grade__cut">CUT &amp; SIFTED</div>
      <div class="grade__organic">ORGANIC</div>
    </div>

    <div class="product">
      <div class="product__name">BRINDLEWORT</div>
      <div class="product__sub">ORGANIC</div>
    </div>

    <div class="clear-window" role="img" aria-label="Clear window showing the dried cut and sifted herb leaves inside"></div>

    <div class="net-weight">NET WT. 1.27 OZ (36g)</div>
  </main>
</body>
</html>
```